Business cards for a tribute and obituary website

Our website is called Quiet Orchard.

It is a special place online for people to remember their loved ones who have passed away, through obituaries and tributes. Friends and family can also convey their condolences on the deceased's memorial page. Celebrating the life of the deceased and remembering their legacy is very important to us – death should not be just about grieving.

We would like the card to look tasteful and modern. The design should ideally not have colours that are too bright. The logo and website URL, www.quietorchardpages.net should be visible on the front of the card, with our slogan "Celebrating a life passed" on the back.

The design should communicate our purpose – remembering loved ones who have passed – and also a lighter tone of celebrating life. It should not look like a funeral director's card!

Our logo has been attached. Looking forward to some beautiful designs! Get creative :)
Updates

Reason: Thank you all for your designs. The rest of my team and I have not reached a decision on which design to select and I am collecting feedback from them. I will provide feedback for any changes that need to be made soon. It would be great if we could see more original designs and in more colours! We will definitely select a design by this deadline.

Industry/Entity Type

Business

Contact Information for Business Card

Nadia Fenwick
Project Manager
471226809
nadiafenwick@quietorchardpages.net

Font styles to use
Serif
Sans Serif

Requirements
Must have
• Logo and website address (www.quietorchardpages.net) on the front.
Nice to have
• Hi designers! It would be nice to see alternative colours – feel free to try out colours that are tasteful and subtle. The colour of the business card does not have to be the same as the logo.
• We would also like to see the logo used in different ways, perhaps a glossy or embossed finish. The card should look stylish.

```html
<!DOCTYPE html>
<html lang="en">
<head>
<meta charset="utf-8">
<title>Quiet Orchard – Business Cards</title>
<link rel="stylesheet" href="https://fonts.googleapis.com/css2?family=Merriweather:wght@700&family=Tinos&display=swap">
<style>
  :root {
    --page-bg: #ece8e4;
    --plum-deep: #6a1a72;
    --plum-mid: #7d3488;
    --plum-soft: #8a4a94;
    --lilac-band: #9c63a6;
    --lilac-tab: #a873b0;
    --paper: #ffffff;
    --ink-light: #ffffff;
  }
  * { box-sizing: border-box; margin: 0; padding: 0; }
  html, body { width: 1200px; height: 892px; overflow: hidden; }
  body {
    background: var(--page-bg);
    position: relative;
    font-family: "Tinos", "Times New Roman", serif;
    color: var(--ink-light);
  }
  .card {
    position: absolute;
    width: 560px;
    height: 320px;
    background: var(--paper);
    overflow: hidden;
    box-shadow: 0 6px 18px rgba(60, 40, 60, 0.18);
  }
  .card--back { left: 570px; top: 90px; }
  .card--front { left: 70px; top: 480px; }

  .card__field {
    position: absolute;
    left: 0; right: 0;
    background: linear-gradient(100deg, var(--plum-deep) 0%, var(--plum-mid) 55%, var(--plum-soft) 100%);
  }
  .card--back .card__field { top: 30px; bottom: 0; }
  .card--front .card__field { top: 30px; height: 206px; }

  .brand {
    position: absolute;
    left: 0; right: 0;
    text-align: center;
  }
  .brand__dot {
    display: block;
    width: 44px; height: 44px;
    margin: 0 auto 12px;
    border-radius: 50%;
    border: 3px solid var(--ink-light);
  }
  .brand__name {
    font-family: "Merriweather", Georgia, serif;
    font-weight: 700;
    font-size: 25px;
    line-height: 1.05;
    letter-spacing: 0.5px;
  }
  .card--back .brand { top: 62px; }
  .card--front .brand { top: 50px; }

  .slogan { font-size: 15px; margin-top: 6px; }

  .band {
    position: absolute;
    left: 0; right: 0;
    top: 212px; bottom: 0;
    background: var(--lilac-band);
    border-top: 2px solid var(--paper);
    display: flex;
    align-items: center;
    justify-content: center;
  }
  .url { font-size: 15px; letter-spacing: 0.3px; }

  .contact {
    position: absolute;
    left: 0; right: 0;
    top: 164px;
    text-align: center;
    font-size: 15px;
    line-height: 1.3;
  }

  .name-tab {
    position: absolute;
    left: 0; top: 0;
    width: 560px; height: 320px;
  }
  .person {
    position: absolute;
    left: 150px;
    top: 238px;
    width: 230px;
    text-align: center;
  }
  .person__name { font-size: 26px; line-height: 1.1; }
  .person__role { font-size: 13px; margin-top: 4px; }
</style>
</head>
<body>

  <section class="card card--back" aria-label="Card back">
    <div class="card__field"></div>
    <div class="brand">
      <span class="brand__dot"></span>
      <div class="brand__name">Quiet<br>Orchard</div>
      <div class="slogan">Celebrating a life passed</div>
    </div>
    <div class="band">
      <span class="url">www.quietorchardpages.net</span>
    </div>
  </section>

  <section class="card card--front" aria-label="Card front">
    <div class="card__field"></div>
    <svg class="name-tab" viewBox="0 0 560 320" aria-hidden="true">
      <polygon points="95,262 150,226 372,226 412,304 95,304" fill="var(--lilac-tab)"/>
    </svg>
    <div class="brand">
      <span class="brand__dot"></span>
      <div class="brand__name">Quiet<br>Orchard</div>
    </div>
    <div class="contact">
      <div>www.quietorchardpages.net</div>
      <div>nadiafenwick@quietorchardpages.net</div>
    </div>
    <div class="person">
      <div class="person__name">Nadia Fenwick</div>
      <div class="person__role">Project Manager</div>
    </div>
  </section>

</body>
</html>
```